LEARN Business Skills so you can Earn a good living

size of the poster is 8”x 10.75" plus 0.25" bleed.
Please leave 1 inch on the bottoum for footer
I want a design a poster that will attract people's attention.
I appreciate a creative ad however the ad should not take away from being able to clearly read the text.
-I also appreciate a simple creative ad that is not too busy.
-you can use graphics, vectors, or pictures of real people.
-however, if you use real people it should be a white male that is wearing a white shirt and look like a professional person.

Target Market(s)

Potential young business people

Industry/Entity Type

education

Requirements
Must have
• easy to read the text
Nice to have
• I would like a "creative" simple ad that is easy to be read
Should not have
• pictures of women

```html
<!DOCTYPE html>
<html lang="en">
<head>
<meta charset="UTF-8">
<title>Learn It To Earn It – Business Enrichment Course</title>
<link href="https://fonts.googleapis.com/css2?family=Montserrat:wght@500;600;800;900&display=swap" rel="stylesheet">
<style>
  :root {
    --navy: #1e1e52;
    --gold: #f0b944;
    --white: #ffffff;
    --ink: #0c0c14;
    --backdrop: #5b5b5b;
  }
  * { margin: 0; padding: 0; box-sizing: border-box; }
  html, body { width: 1200px; height: 1200px; overflow: hidden; }
  body {
    background: var(--backdrop);
    font-family: "Montserrat", Arial, sans-serif;
    position: relative;
  }
  .poster {
    position: absolute;
    left: 195px; top: 88px;
    width: 810px; height: 1024px;
    background: var(--white);
    overflow: hidden;
  }
  .masthead {
    position: absolute; left: 0; top: 0;
    width: 810px; height: 264px;
    background: var(--navy);
    text-align: center;
  }
  .masthead .line {
    display: block;
    font-weight: 900;
    font-size: 104px;
    line-height: 1;
    letter-spacing: 1px;
  }
  .masthead .learn { color: var(--gold); padding-top: 40px; }
  .masthead .earn { color: var(--white); margin-top: -2px; }

  .feature-panel {
    position: absolute; left: 0; top: 264px;
    width: 810px; height: 544px;
    background: var(--gold);
  }
  .course-title {
    position: absolute; left: 92px; top: 16px;
    font-weight: 900; font-size: 40px; color: var(--ink);
    white-space: nowrap;
  }
  .benefit {
    position: absolute; left: 92px;
    display: flex;
    align-items: flex-start;
  }
  .benefit .icon { width: 72px; flex: none; display: block; }
  .benefit p {
    margin-left: 20px;
    font-weight: 600; color: var(--ink);
    font-size: 29px; line-height: 35px;
    white-space: nowrap;
  }
  .benefit.first { top: 85px; }
  .benefit.second { top: 225px; }
  .benefit.third { top: 367px; }
  .benefit.third .icon { margin-top: 6px; }
  .benefit.third p { font-size: 31px; line-height: 38px; }
  .divider {
    position: absolute; left: 183px;
    width: 216px; height: 0;
    border-top: 3px dotted var(--ink);
  }
  .divider.one { top: 208px; }
  .divider.two { top: 349px; }
  .presenter-photo {
    position: absolute; left: 564px; top: 80px;
    width: 246px; height: 464px;
    background: linear-gradient(180deg, #e6b37f 0%, #2a2a2e 40%, #1c1c20 100%);
    border-radius: 120px 120px 0 0;
  }

  .topics {
    position: absolute; left: 0; top: 808px;
    width: 810px; height: 120px;
    background: var(--navy);
    color: var(--white);
    font-weight: 500; font-size: 14px; line-height: 17.6px;
    text-align: center;
    padding: 20px 50px 0;
  }
  .footer-space {
    position: absolute; left: 0; top: 928px;
    width: 810px; height: 96px;
    background: var(--white);
  }
</style>
</head>
<body>
<main class="poster">
  <header class="masthead">
    <span class="line learn">LEARN IT</span>
    <span class="line earn">TO EARN IT</span>
  </header>

  <section class="feature-panel">
    <h1 class="course-title">Business Enrichment Course</h1>

    <div class="benefit first">
      <svg class="icon" viewBox="0 0 72 72" fill="none" stroke="var(--navy)" stroke-width="4" stroke-linejoin="round" stroke-linecap="round">
        <path d="M4 30 L22 12 L34 20 L46 10 L68 32 L40 60 Q34 66 28 60 L8 40 Z"/>
        <path d="M34 20 L24 30 Q28 36 34 30 L40 26 L56 42"/>
        <path d="M24 48 L34 38 M30 54 L40 44 M36 58 L46 48"/>
      </svg>
      <p>A proven success of<br>helping people in their<br>livelihoods</p>
    </div>

    <div class="divider one"></div>

    <div class="benefit second">
      <svg class="icon" viewBox="0 0 72 80" fill="none" stroke="var(--navy)" stroke-width="4" stroke-linejoin="round">
        <g transform="translate(18 20)">
          <circle r="6"/>
          <path d="M-3 -15 H3 L4 -10 L9 -7 L13 -10 L16 -5 L12 -1 V4 L16 7 L13 12 L9 9 L4 12 L3 16 H-3 L-4 12 L-9 9 L-13 12 L-16 7 L-12 4 V-1 L-16 -5 L-13 -10 L-9 -7 L-4 -10 Z"/>
        </g>
        <g transform="translate(48 54) scale(1.35)">
          <circle r="6"/>
          <path d="M-3 -15 H3 L4 -10 L9 -7 L13 -10 L16 -5 L12 -1 V4 L16 7 L13 12 L9 9 L4 12 L3 16 H-3 L-4 12 L-9 9 L-13 12 L-16 7 L-12 4 V-1 L-16 -5 L-13 -10 L-9 -7 L-4 -10 Z"/>
        </g>
      </svg>
      <p>Business<br>skills that will<br>help you</p>
    </div>

    <div class="divider two"></div>

    <div class="benefit third">
      <svg class="icon" viewBox="0 0 72 52" fill="none" stroke="var(--navy)" stroke-width="4" stroke-linejoin="round">
        <rect x="10" y="4" width="58" height="36" rx="2"/>
        <circle cx="39" cy="22" r="8" fill="var(--navy)"/>
        <path d="M18 12 Q22 12 22 8 M60 12 Q56 12 56 8 M18 32 Q22 32 22 36 M60 32 Q56 32 56 36"/>
        <path d="M4 14 V48 H62"/>
      </svg>
      <p>Get a quality<br>job - start/grow<br>your business-Increase<br>your salary</p>
    </div>

    <div class="presenter-photo" role="img" aria-label="Photo of a smiling young businessman in glasses, dark suit and white shirt, pointing toward the benefits list"></div>
  </section>

  <section class="topics">
    BUSINESS ADMIISTRATION – SMALL BUSINESS MANAGEMENT - FINANCE - INVESTMENTS -<br>
    COMPUTERS- ACCOUNTING - SALES - MARKETING - PROJECT MANAGEMENT INTERVIEWING<br>
    SKILLS - BUSINESS LAW -NEGOTIATION -- PUBLIC SPEAKING - &nbsp;- IMPORT/EXPORT -<br>
    INFORMATION TECHNOLOY -DISTRIBUTION - MARKETING - &nbsp;LEDGERLY - REAL ESTATE -<br>
    HEALTH CARE-MANAGEMENT - SHOPNEST
  </section>

  <footer class="footer-space"></footer>
</main>
</body>
</html>
```